Velmora Supply Chain and Logistic Consulting

Please review the attached Business Card. I want as close to this card with the colors, fonts, and quality of the card as possible. The attached compass should replace the deer head on both sides of the card and the text should say:

Backside
Compass JPEG
Velmora SC&L
A Supply Chain and Logistics Consulting Company

Frontside
Velmora SC&L
Ravi Ostrander - Tampa Florida
President
____________________________________
(727) 555-0193
VelmoraSCL@Quillpost.com
_____________________________________

Bottom Front Side

Target Market(s)

Businesses

Contact Information for Business Card

Backside
Compass JPEG
Velmora SC&L

Frontside
Velmora SC&L
President
(727) 555-0193
VelmoraSCL@Quillpost.com

Bottom Front Side

Font styles to use
Serif
Script

Colors

Designer to choose colors to be used in the design.

Requirements
Must have
• See attached card for reference
Nice to have
Should not have

```html
<!DOCTYPE html>
<html lang="en">
<head>
<meta charset="utf-8">
<title>Velmora SC&amp;L — Business Card</title>
<link rel="stylesheet" href="https://fonts.googleapis.com/css2?family=Merriweather:wght@300;400&family=Cormorant+Garamond:wght@400;500&display=swap">
<style>
  :root {
    --canvas: #d2d2d2;
    --card: #1e1c1d;
    --ink: #f2f2f2;
    --ink-soft: #bdbdbd;
    --rule: #6a6a6a;
    --mark-light: #cfcfcf;
    --mark-dark: #5a5a5a;
  }
  html, body {
    margin: 0;
    width: 1200px;
    height: 815px;
    overflow: hidden;
    background: radial-gradient(ellipse at center, #e4e4e4 0%, var(--canvas) 70%, #bcbcbc 100%);
  }
  .sheet {
    position: relative;
    width: 1200px;
    height: 815px;
    display: flex;
    align-items: center;
    justify-content: center;
    gap: 40px;
  }
  .card {
    position: relative;
    width: 540px;
    height: 309px;
    background: var(--card);
    border-radius: 26px;
    box-shadow: 0 14px 30px rgba(0,0,0,0.35);
    color: var(--ink);
    overflow: hidden;
    font-family: "Merriweather", Georgia, serif;
  }
  .company-name {
    font-family: "Merriweather", Georgia, serif;
    font-weight: 400;
    color: var(--ink);
    margin: 0;
    text-align: center;
    white-space: nowrap;
  }
  .tagline {
    font-family: "Cormorant Garamond", Georgia, serif;
    font-size: 9px;
    letter-spacing: 0.6px;
    text-transform: uppercase;
    text-align: center;
    color: var(--ink-soft);
    margin: 4px 0 0;
  }
  .rule {
    height: 1px;
    background: linear-gradient(90deg, transparent, var(--rule) 15%, var(--rule) 85%, transparent);
  }

  /* front */
  .card-front .corner-mark {
    position: absolute;
    top: -40px;
    right: -40px;
    width: 170px;
    height: 170px;
    border-radius: 50%;
    background: radial-gradient(circle, rgba(110,110,110,0.28) 0%, rgba(70,70,70,0.14) 55%, transparent 72%);
  }
  .card-front .block {
    position: absolute;
    left: 0;
    right: 0;
    top: 46px;
    display: flex;
    flex-direction: column;
    align-items: center;
  }
  .card-front .company-name { font-size: 24px; }
  .card-front .rule { width: 320px; margin: 8px 0 10px; }
  .person { font-size: 15px; letter-spacing: 0.4px; margin: 0; }
  .role { font-family: "Cormorant Garamond", Georgia, serif; font-size: 13px; color: var(--ink-soft); margin: 3px 0 0; }
  .phone { font-size: 15px; letter-spacing: 0.8px; margin: 0; }
  .email { font-size: 11px; letter-spacing: 2.4px; color: var(--ink-soft); margin: 8px 0 0; }
  .socials { display: flex; align-items: center; gap: 8px; margin-top: 8px; }
  .socials .dot { width: 8px; height: 8px; border-radius: 50%; background: var(--ink); }
  .socials .sep { width: 1px; height: 9px; background: var(--ink-soft); }
  .socials .rule { width: 110px; margin: 0; }
  .card-front .rule.end { width: 300px; margin: 16px 0 0; }

  /* back */
  .card-back .compass {
    position: absolute;
    left: 50%;
    top: 42px;
    width: 150px;
    height: 150px;
    margin-left: -75px;
    border-radius: 50%;
    background: radial-gradient(circle, var(--mark-light) 0%, var(--mark-dark) 70%, var(--card) 100%);
  }
  .card-back .title {
    position: absolute;
    left: 0;
    right: 0;
    top: 214px;
  }
  .card-back .company-name { font-size: 26px; }
</style>
</head>
<body>
<main class="sheet">
  <section class="card card-front" aria-label="Card front">
    <div class="corner-mark" role="img" aria-label="Faint compass rose decoration"></div>
    <div class="block">
      <h1 class="company-name">Velmora SC&amp;L</h1>
      <p class="tagline">A Supply Chain and Logistics Consulting Company</p>
      <div class="rule"></div>
      <p class="person">Ravi Ostrander - Tampa Florida</p>
      <p class="role">President</p>
      <div class="rule"></div>
      <p class="phone">(727) 555-0193</p>
      <p class="email">VelmoraSCL@Quillpost.com</p>
      <div class="socials">
        <span class="rule"></span>
        <span class="dot"></span>
        <span class="sep"></span>
        <span class="dot"></span>
        <span class="rule"></span>
      </div>
      <div class="rule end"></div>
    </div>
  </section>

  <section class="card card-back" aria-label="Card back">
    <div class="compass" role="img" aria-label="Silver compass rose with N, E, S, W bearings"></div>
    <div class="title">
      <h2 class="company-name">Velmora SC&amp;L</h2>
      <p class="tagline">A Supply Chain and Logistics Consulting Company</p>
    </div>
  </section>
</main>
</body>
</html>
```